Price Calculator as Responsive Web App to support Sales People

We need to build a simple micro web app to support sales people in making quotes. We already have a backend that can take a number of parameters and create a quote. We need put a responsive web app on top of this so that our people on the road can easily do their price simulations.

We need two pages. One for the input and another for the results. No menus, navigations, etc. It is 6 different inputs as shown with boxes in the sketch. They don't need to be boxed, but some of them have a bit of instruction text that clearly need to belong to the input.

This needs to be responsive, but first and foremost designed for smartphones. I have included a background gradient that we would like to use -- or a variant of it. We expect this to be delivered as HTML/CSS + images so that we can quickly write a few pieces of JavaScript ourselves to wire it up to our price simulator.

Industry/Entity Type

Information Technology

Coding

Coded - Design and coding required

Number of Pages Required

2 page

Font styles to use
Sans Serif

Requirements
Must have
• Responsive design
• Easy to wire up JavaScript to the HTML/CSS
Nice to have
• Some quick way to pick number of months. +/- buttons to add remove a year or 3 months. Same thing with number of items. Add 10 or 5 quickly.
• Maybe some parallax effect while scrolling as long as it is not distracting.
Should not have
• Toolbars, Menus, Navigations, Banners, etc. This is just a single micro app.

```html
<!DOCTYPE html>
<html lang="en">
<head>
<meta charset="utf-8">
<title>Price Calculator</title>
<link rel="stylesheet" href="https://fonts.googleapis.com/css2?family=Open+Sans:wght@400;600;700&display=swap">
<style>
:root{
  --page-bg:#e4e4e4;
  --panel-bg:#ffffff;
  --navy:#0d3a63;
  --text:#333a40;
  --border:#c9c9c9;
  --radio:#8e8e8e;
  --shadow:rgba(0,0,0,0.12);
}
*{box-sizing:border-box;margin:0;padding:0}
html,body{width:1059px;height:1200px;overflow:hidden}
body{background:var(--page-bg);font-family:"Open Sans",Arial,sans-serif;color:var(--text);position:relative}
.panel{position:absolute;background:var(--panel-bg);box-shadow:0 2px 4px var(--shadow)}
.panel--duration{left:18px;top:28px;width:504px;height:119px}
.panel--count{left:537px;top:28px;width:504px;height:119px}
.panel--engine{left:18px;top:161px;width:1023px;height:296px}
.panel--storage{left:18px;top:470px;width:1023px;height:246px}
.panel--tip{left:18px;top:730px;width:1023px;height:217px}
.panel--elastic{left:18px;top:963px;width:1023px;height:217px}

.field-label{position:absolute;top:46px;font-size:22px;font-weight:600;color:var(--navy);letter-spacing:.3px;line-height:30px}
.panel--duration .field-label{left:37px}
.panel--count .field-label{left:41px}

.stepper{position:absolute;top:33px;width:243px;height:60px;display:flex;border:1px solid #b9b9b9;border-radius:3px;background:#fff;box-shadow:0 3px 3px rgba(0,0,0,0.18)}
.panel--duration .stepper{left:222px}
.panel--count .stepper{left:216px}
.stepper__btn{width:80px;display:flex;align-items:center;justify-content:center;background:#f7f7f7}
.stepper__value{flex:1;display:flex;align-items:center;justify-content:center;font-size:27px;color:var(--text);border-left:1px solid #b9b9b9;border-right:1px solid #b9b9b9}

.section-title{position:absolute;left:30px;display:flex;align-items:center;gap:22px;font-size:22px;font-weight:600;color:var(--navy);letter-spacing:.3px}
.section-title svg{width:20px;height:20px;fill:var(--navy)}
.panel--engine .section-title{top:37px}
.panel--storage .section-title{top:37px}
.panel--tip .section-title{top:37px}
.panel--elastic .section-title{top:37px}

.options{position:absolute;left:36px;display:flex;gap:11px}
.panel--engine .options{top:92px}
.panel--storage .options{top:98px;gap:12px}
.panel--tip .options{top:99px;gap:12px}
.panel--elastic .options{top:97px;left:40px;gap:20px}

.option{background:#fff;border:1px solid var(--border);display:flex;align-items:center;gap:16px;padding-left:24px;font-size:22px;color:var(--text)}
.option--selected{background:var(--navy);border-color:var(--navy);color:#fff}
.option__radio{width:26px;height:26px;border-radius:50%;border:2px solid var(--radio);background:#fafafa;flex:none}
.option__check{width:22px;height:22px;flex:none}
.option__text{line-height:29px}
.option__text strong{display:block;font-weight:700}

.panel--engine .option{width:232px;height:89px}
.panel--storage .option,.panel--tip .option{width:182px;height:77px}
.panel--elastic .option{width:180px;height:78px}
.option--wide{padding-left:20px}

.range-hint{position:absolute;left:231px;top:202px;width:182px;text-align:center;font-size:17px;font-weight:700;color:var(--navy);letter-spacing:.3px}
.help-text{position:absolute;font-size:21px;line-height:35px;color:var(--text)}
.panel--engine .help-text{left:41px;top:215px}
.panel--elastic .help-text{left:493px;top:96px;width:480px}
</style>
</head>
<body>

<section class="panel panel--duration">
  <span class="field-label">DURATION</span>
  <div class="stepper">
    <div class="stepper__btn">
      <svg width="32" height="34" viewBox="0 0 32 34" fill="none" stroke="#0d3a63" stroke-width="2"><rect x="3" y="5" width="26" height="26" rx="2"/><path d="M9 2v6M16 2v6M23 2v6"/><circle cx="16" cy="19" r="7"/><path d="M12 19h8"/></svg>
    </div>
    <div class="stepper__value">24</div>
    <div class="stepper__btn">
      <svg width="32" height="34" viewBox="0 0 32 34" fill="none" stroke="#0d3a63" stroke-width="2"><rect x="3" y="5" width="26" height="26" rx="2"/><path d="M9 2v6M16 2v6M23 2v6"/><circle cx="16" cy="19" r="7"/><path d="M12 19h8M16 15v8"/></svg>
    </div>
  </div>
</section>

<section class="panel panel--count">
  <span class="field-label">COUNT</span>
  <div class="stepper">
    <div class="stepper__btn">
      <svg width="24" height="24" viewBox="0 0 24 24" fill="none" stroke="#0d3a63" stroke-width="2"><rect x="2" y="2" width="20" height="20" rx="4"/><path d="M7 12h10"/></svg>
    </div>
    <div class="stepper__value">100</div>
    <div class="stepper__btn">
      <svg width="24" height="24" viewBox="0 0 24 24" fill="none" stroke="#0d3a63" stroke-width="2"><rect x="2" y="2" width="20" height="20" rx="4"/><path d="M7 12h10M12 7v10"/></svg>
    </div>
  </div>
</section>

<section class="panel panel--engine">
  <h2 class="section-title">
    <svg viewBox="0 0 20 20"><path d="M8.6 0h2.8l.5 2.6 1.9.8 2.2-1.5 2 2-1.5 2.2.8 1.9 2.7.5v2.8l-2.7.5-.8 1.9 1.5 2.2-2 2-2.2-1.5-1.9.8-.5 2.7H8.6l-.5-2.7-1.9-.8-2.2 1.5-2-2 1.5-2.2-.8-1.9L0 11.4V8.6l2.7-.5.8-1.9L2 4l2-2 2.2 1.5 1.9-.8zM10 6.5a3.5 3.5 0 100 7 3.5 3.5 0 000-7z"/></svg>
    ENGINE POWER
  </h2>
  <div class="options">
    <div class="option"><span class="option__radio"></span><span class="option__text"><strong>360$/Year</strong>Bonze Power</span></div>
    <div class="option option--selected option--wide"><svg class="option__check" viewBox="0 0 22 22"><path d="M3 11.5l5 5L19 5.5" fill="none" stroke="#fff" stroke-width="3.4"/></svg><span class="option__text"><strong>600$/Year</strong>Silver Power</span></div>
    <div class="option"><span class="option__radio"></span><span class="option__text"><strong>1M$/Year</strong>Gold Power</span></div>
    <div class="option"><span class="option__radio"></span><span class="option__text"><strong>3M$/Year</strong>Platinum Super</span></div>
  </div>
  <p class="help-text">Lorem Ipsum is simply dummy text of the printing and typesetting industry</p>
</section>

<section class="panel panel--storage">
  <h2 class="section-title">
    <svg viewBox="0 0 20 20"><ellipse cx="10" cy="3.5" rx="8" ry="3"/><path d="M2 6.5c0 1.7 3.6 3 8 3s8-1.3 8-3v3.5c0 1.7-3.6 3-8 3s-8-1.3-8-3zM2 11.5c0 1.7 3.6 3 8 3s8-1.3 8-3V15c0 1.7-3.6 3-8 3s-8-1.3-8-3z"/></svg>
    SHARED STORAGE ADDITION
  </h2>
  <div class="options">
    <div class="option"><span class="option__radio"></span><span class="option__text">10 kg</span></div>
    <div class="option option--selected option--wide"><svg class="option__check" viewBox="0 0 22 22"><path d="M3 11.5l5 5L19 5.5" fill="none" stroke="#fff" stroke-width="3.4"/></svg><span class="option__text">50 kg</span></div>
    <div class="option"><span class="option__radio"></span><span class="option__text">100 kg</span></div>
    <div class="option"><span class="option__radio"></span><span class="option__text">500 kg</span></div>
    <div class="option"><span class="option__radio"></span><span class="option__text">1T</span></div>
  </div>
  <span class="range-hint">203-2118 KG</span>
</section>

<section class="panel panel--tip">
  <h2 class="section-title">
    <svg viewBox="0 0 20 20"><path d="M7.5 1h5v6.5H19v5h-6.5V19h-5v-6.5H1v-5h6.5z"/></svg>
    ADDITIONAL TIP
  </h2>
  <div class="options">
    <div class="option"><span class="option__radio"></span><span class="option__text">15%</span></div>
    <div class="option option--selected option--wide"><svg class="option__check" viewBox="0 0 22 22"><path d="M3 11.5l5 5L19 5.5" fill="none" stroke="#fff" stroke-width="3.4"/></svg><span class="option__text">18%</span></div>
    <div class="option"><span class="option__radio"></span><span class="option__text">20%</span></div>
  </div>
</section>

<section class="panel panel--elastic">
  <h2 class="section-title">
    <svg viewBox="0 0 20 20"><path d="M19 2.4L17.6 1 12.5 6.1V3h-2v6.5H17v-2h-3.1zM1 17.6L2.4 19l5.1-5.1V17h2v-6.5H3v2h3.1z"/></svg>
    ELASTIC EXTENSION
  </h2>
  <div class="options">
    <div class="option option--selected option--wide"><svg class="option__check" viewBox="0 0 22 22"><path d="M3 11.5l5 5L19 5.5" fill="none" stroke="#fff" stroke-width="3.4"/></svg><span class="option__text">30%</span></div>
    <div class="option"><span class="option__radio"></span><span class="option__text">50%</span></div>
  </div>
  <p class="help-text">Lorem Ipsum is simply dummy text of the printing and typesetting industry</p>
</section>

</body>
</html>
```